2 Creative Website Banners for Furniture Brand

Morning Tobrasca....
The get a great night sleep banner is complete - we are happy with that one.
Ive uploaded a slightly different concept for the other banner below. This is just something rough ive thrown together. But you can see I have added a curve, a maroon coloured background which is slightly transparent and a big heart in the background....
I do not necessarily want to use this heart image but something a bit like this (a nice graphic, gif etc) but something quite elegant faded in, or perhaps a number of hearts (done in a tasteful way). Also can we keep the typography in the same format as you can see for this one.
Nearly there :)!
Industry/Entity Type
Furniture

```html
<!DOCTYPE html>
<html lang="en">
<head>
<meta charset="utf-8">
<title>Lunierre Furniture</title>
<link rel="stylesheet" href="https://fonts.googleapis.com/css2?family=Cinzel:wght@400&family=Montserrat:wght@400;500&family=Oswald:wght@400&display=swap">
<style>
  :root {
    --notice-bg: #e4dccd;
    --notice-text: #8c7a52;
    --ink: #3a2a33;
    --brand: #3d1f35;
    --accent-gold: #c9a33a;
    --nav-bg: #9d8c80;
    --white: #ffffff;
    --maroon-veil: rgba(112, 28, 52, 0.62);
    --card-taupe: #bcb09e;
    --card-photo: #e6e4e1;
    --heart-btn: #8b7b6e;
    --button-text: #5a4a40;
  }
  * { box-sizing: border-box; margin: 0; padding: 0; }
  html, body { width: 1200px; height: 626px; overflow: hidden; background: var(--white); }
  body { font-family: "Montserrat", Arial, sans-serif; color: var(--ink); position: relative; }

  .notice-bar {
    position: absolute; left: 0; top: 0; width: 1200px; height: 24px;
    background: var(--notice-bg); color: var(--notice-text);
    font-size: 10.5px; line-height: 24px; text-align: center; letter-spacing: 0.1px;
  }

  .site-header { position: absolute; left: 0; top: 24px; width: 1200px; height: 96px; }
  .brand-name {
    position: absolute; left: 6px; top: 32px;
    font-family: "Montserrat", Arial, sans-serif; font-weight: 400;
    font-size: 31px; letter-spacing: 10px; color: var(--brand);
  }
  .phone {
    position: absolute; left: 940px; top: 10px; display: flex; align-items: center; gap: 10px;
    font-size: 24px; letter-spacing: 0.6px; color: var(--ink);
  }
  .phone-dot { width: 23px; height: 23px; border-radius: 50%; background: var(--brand); }
  .account-links {
    position: absolute; left: 844px; top: 63px; display: flex; gap: 18px;
    font-size: 11px; color: var(--ink); letter-spacing: 0.3px;
  }
  .account-links li { list-style: none; display: flex; align-items: center; gap: 5px; }
  .account-links svg { display: block; }

  .main-nav {
    position: absolute; left: 0; top: 120px; width: 1200px; height: 42px; background: var(--nav-bg);
  }
  .main-nav a {
    position: absolute; top: 0; line-height: 42px; color: var(--white);
    font-size: 14px; text-decoration: none; display: flex; align-items: center; gap: 8px;
  }

  .hero { position: absolute; left: 0; top: 162px; width: 1200px; height: 356px; overflow: hidden; }
  .hero svg { position: absolute; left: 0; top: 0; }
  .hero-kicker {
    position: absolute; left: 89px; top: 88px; font-family: "Cinzel", Georgia, serif;
    font-size: 31px; line-height: 1; color: var(--white); letter-spacing: 1.5px;
  }
  .hero-title {
    position: absolute; left: 86px; top: 134px; font-family: "Cinzel", Georgia, serif;
    font-size: 94px; line-height: 1; color: var(--white); letter-spacing: 10px;
  }
  .shop-now {
    position: absolute; left: 171px; top: 248px; width: 128px; height: 42px;
    background: var(--white); border-radius: 7px; text-align: center;
    font-family: "Oswald", Arial, sans-serif; font-size: 25px; line-height: 42px;
    color: var(--button-text); text-decoration: none;
  }

  .category-row { position: absolute; left: 0; top: 556px; width: 1200px; height: 70px; }
  .category-card { position: absolute; top: 0; width: 222px; height: 70px; border-radius: 3px 3px 0 0; }
  .category-card.is-feature { background: var(--card-taupe); }
  .category-card.is-feature::after {
    content: ""; position: absolute; left: 6px; top: 6px; right: 6px; bottom: -6px;
    border: 1px solid rgba(255,255,255,0.8);
  }
  .category-card.is-photo { background: linear-gradient(180deg, #f1f0ee, var(--card-photo)); }

  .security-badge {
    position: absolute; left: 1138px; top: 560px; width: 62px; height: 54px;
    background: #f4f4f4; box-shadow: 0 0 3px rgba(0,0,0,0.3);
  }
  .wishlist-fab {
    position: absolute; left: 1157px; top: 582px; width: 36px; height: 36px;
    background: var(--heart-btn); display: flex; align-items: center; justify-content: center;
  }
</style>
</head>
<body>
  <div class="notice-bar">COVID 19 - WE ARE TAKING ORDERS AND DELIVERING AS NORMAL</div>

  <header class="site-header">
    <div class="brand-name">LUNIERRE</div>
    <div class="phone"><span class="phone-dot"></span>0345 210 7781</div>
    <ul class="account-links">
      <li><svg width="14" height="14" viewBox="0 0 14 14"><circle cx="7" cy="7" r="5.5" fill="none" stroke="#c9a33a" stroke-width="2"/></svg>TRACK ORDER</li>
      <li><svg width="16" height="14" viewBox="0 0 16 14"><path d="M8 13 L1.5 6.5 A3.6 3.6 0 0 1 8 2.5 A3.6 3.6 0 0 1 14.5 6.5 Z" fill="#c9a33a"/></svg>MY WISHLIST</li>
      <li><svg width="15" height="17" viewBox="0 0 15 17"><rect x="1" y="5" width="13" height="11" fill="none" stroke="#c9a33a" stroke-width="1.6"/><path d="M4.5 5 V3.5 A3 3 0 0 1 10.5 3.5 V5" fill="none" stroke="#c9a33a" stroke-width="1.6"/></svg>CART &nbsp;(0)</li>
    </ul>
  </header>

  <nav class="main-nav">
    <a href="#" style="left:74px">HOME</a>
    <a href="#" style="left:229px">BEDROOM <svg width="10" height="6" viewBox="0 0 10 6"><path d="M1 1 L5 5 L9 1" fill="none" stroke="#fff" stroke-width="1.6"/></svg></a>
    <a href="#" style="left:433px">LIVING ROOM <svg width="10" height="6" viewBox="0 0 10 6"><path d="M1 1 L5 5 L9 1" fill="none" stroke="#fff" stroke-width="1.6"/></svg></a>
    <a href="#" style="left:660px">DINING ROOM <svg width="10" height="6" viewBox="0 0 10 6"><path d="M1 1 L5 5 L9 1" fill="none" stroke="#fff" stroke-width="1.6"/></svg></a>
    <a href="#" style="left:890px">CONTACT <svg width="10" height="6" viewBox="0 0 10 6"><path d="M1 1 L5 5 L9 1" fill="none" stroke="#fff" stroke-width="1.6"/></svg></a>
  </nav>

  <section class="hero">
    <svg width="1200" height="356" viewBox="0 0 1200 356">
      <defs>
        <linearGradient id="heroDark" x1="0" y1="0" x2="1" y2="1">
          <stop offset="0" stop-color="#5a4f4a"/>
          <stop offset="1" stop-color="#3f3532"/>
        </linearGradient>
        <linearGradient id="heroGold" x1="0" y1="0" x2="1" y2="1">
          <stop offset="0" stop-color="#f6e09a"/>
          <stop offset="0.5" stop-color="#e0b45a"/>
          <stop offset="1" stop-color="#8f5f26"/>
        </linearGradient>
        <path id="heartShape" d="M0 12 L-11 1 A6.2 6.2 0 0 1 0 -6 A6.2 6.2 0 0 1 11 1 Z"/>
      </defs>
      <rect width="1200" height="356" fill="url(#heroGold)" role="img" aria-label="Bright luxury bedroom with chandelier, city-view windows and a tufted bed"/>
      <path class="maroon-veil" d="M0 0 H640 C760 90 760 266 640 356 H0 Z" fill="url(#heroDark)" role="img" aria-label="Dimly lit bedroom with an upholstered bed and soft throws"/>
      <path d="M0 0 H640 C760 90 760 266 640 356 H0 Z" fill="#701c34" fill-opacity="0.55"/>
      <g class="faded-hearts" fill="#ffffff">
        <use href="#heartShape" transform="translate(520 150) scale(7)" fill-opacity="0.07"/>
        <use href="#heartShape" transform="translate(440 60) scale(2.2)" fill-opacity="0.09"/>
        <use href="#heartShape" transform="translate(600 290) scale(2.6)" fill-opacity="0.08"/>
        <use href="#heartShape" transform="translate(40 300) scale(1.8)" fill-opacity="0.08"/>
        <use href="#heartShape" transform="translate(350 40) scale(1.2)" fill-opacity="0.1"/>
      </g>
      <path d="M640 0 C760 90 760 266 640 356" fill="none" stroke="#ffffff" stroke-width="3"/>
    </svg>
    <div class="hero-kicker">FIND A LOOK YOU</div>
    <div class="hero-title">LOVE</div>
    <a class="shop-now" href="#">SHOP NOW</a>
  </section>

  <div class="category-row">
    <div class="category-card is-feature" style="left:42px"></div>
    <div class="category-card is-photo" style="left:292px" role="img" aria-label="White bedroom with wardrobe and panelled wall"></div>
    <div class="category-card is-photo" style="left:539px" role="img" aria-label="Living room with grey sofa and wall shelf"></div>
    <div class="category-card is-photo" style="left:788px" role="img" aria-label="Dining room by bright windows"></div>
  </div>

  <div class="security-badge"></div>
  <div class="wishlist-fab">
    <svg width="20" height="18" viewBox="0 0 16 14"><path d="M8 13 L1.5 6.5 A3.6 3.6 0 0 1 8 2.5 A3.6 3.6 0 0 1 14.5 6.5 Z" fill="#ffffff"/></svg>
  </div>
</body>
</html>
```